Clara Whitby Festival Australia and the Velvet Lantern Historic Dance Academy are organising a Siege of Marrowfield Ball on Saturday 11 April 2015.
We need a poster design asap for publication in the 2014 Clara Whitby Festival Australia program.
Pellham Hall, Canberra http://www.civicvenues-example.net/city-services/venue_group/pellham_hall
7.30pm - 11.30pm
Tickets on sale at www.clarawhitbyfestival.example.au

Would like an unlocked .psd file with illustration used included in additional separate file. Private photos or parts of photos of Clara Whitby Regency people from our past festivals at http://pastrevels.example/gallery/index.php?cat=3 can be used. These are not allowed to be used for other people's projects and are subject to copyright.

2015 is the 200 Anniversary of the Siege of Marrowfield
Updates

Dear All

We've had technical issues on the brief and we have to choose our poster design on or by Sunday 6 April, 9am, Australian Eastern Standard Time. 

Designs: You are welcome to use other designs in addition to ours. I just haven't had time to find a really nice 1815 battle scene :)

Target Market(s)

Male and female attendees aged from 18-45
Interested in history, dancing, historical costume

Industry/Entity Type

Festival

Font styles to use
Serif
Script

Requirements
Must have
• Logo from website clarawhitbyfestival.example and the Velvet Lantern logo at velvetlantern.example.au
The event is being organised by the Velvet Lantern Historic Dance Academy and is the main attraction/event of 2015 Clara Whitby Festival Australia.
Must have Clara Whitby Festival Australia 2015 or 2015 Clara Whitby Festival Australia, somehow, the date.
We print our program on Monday - can use a good draft copy that can then be fixed up next week for printing as posters later - will extend date if good copy received that we like.
I have attached some images that you might like to use, but you do not have to use them. This one might be nice sepia?

```html
<!DOCTYPE html>
<html lang="en">
<head>
<meta charset="utf-8">
<title>Siege of Marrowfield Ball</title>
<link rel="stylesheet" href="https://fonts.googleapis.com/css2?family=Cinzel:wght@400;700&family=Pinyon+Script&family=Playfair+Display+SC:wght@700&display=swap">
<style>
  :root {
    --paper: #f1ecdd;
    --paper-edge: #e6dfcb;
    --ink: #5b5753;
    --ink-dark: #3f3c39;
    --sepia-light: #e2d6bf;
    --sepia-mid: #a88f6c;
    --sepia-dark: #4e3f31;
  }
  html, body {
    margin: 0;
    padding: 0;
    width: 924px;
    height: 1200px;
    overflow: hidden;
    background: var(--paper);
  }
  .poster {
    position: relative;
    width: 924px;
    height: 1200px;
    background: radial-gradient(ellipse at 50% 45%, var(--paper) 60%, var(--paper-edge) 100%);
    color: var(--ink);
    font-family: "Cinzel", serif;
  }
  .centered {
    position: absolute;
    left: 0;
    width: 100%;
    text-align: center;
    margin: 0;
  }
  .swords {
    position: absolute;
    left: 442px;
    top: 56px;
    transform: translateX(-50%);
  }
  .title-main {
    top: 92px;
    width: 912px;
    font-family: "Playfair Display SC", serif;
    font-weight: 700;
    font-size: 112px;
    letter-spacing: 2px;
    line-height: 1;
    color: var(--ink);
  }
  .title-of {
    top: 224px;
    font-family: "Pinyon Script", cursive;
    font-size: 40px;
    line-height: 1;
  }
  .title-of .dot {
    display: inline-block;
    width: 6px;
    height: 6px;
    border-radius: 50%;
    background: var(--ink);
    vertical-align: middle;
    margin: 0 40px;
  }
  .title-rule {
    position: absolute;
    left: 263px;
    top: 281px;
    width: 398px;
    height: 2px;
    background: var(--ink);
  }
  .title-sub {
    top: 300px;
    width: 922px;
    font-family: "Cinzel", serif;
    font-weight: 700;
    font-size: 40px;
    line-height: 1;
  }
  .title-sub .cap { font-size: 50px; }
  .event-date {
    top: 360px;
    width: 922px;
    font-weight: 700;
    font-size: 21px;
    letter-spacing: 0.5px;
  }
  .event-date .cap { font-size: 27px; }
  .dancers {
    position: absolute;
    left: 290px;
    top: 395px;
    width: 310px;
    height: 575px;
  }
  .info {
    position: absolute;
    width: 300px;
    transform: translateX(-50%);
    text-align: center;
  }
  .info-label {
    margin: 0;
    font-family: "Cinzel", serif;
    font-weight: 700;
    font-size: 28px;
    line-height: 1.1;
    color: var(--ink-dark);
  }
  .info-label.small { font-size: 22px; }
  .info-value {
    margin: 6px 0 0;
    font-family: "Pinyon Script", cursive;
    font-size: 33px;
    line-height: 1.25;
  }
  .info-value.url {
    font-size: 23px;
    margin-top: 40px;
    white-space: nowrap;
  }
  .venue { left: 166px; top: 548px; }
  .time { left: 161px; top: 716px; }
  .cost { left: 732px; top: 548px; }
  .tickets { left: 732px; top: 709px; }
  .festival-line {
    top: 976px;
    left: 290px;
    width: 326px;
    font-weight: 700;
    font-size: 15px;
    line-height: 1.25;
    color: var(--ink-dark);
  }
  .festival-line .cap { font-size: 19px; }
  .partner {
    position: absolute;
    display: flex;
    align-items: center;
    gap: 14px;
    font-family: "Cinzel", serif;
    font-weight: 700;
    color: var(--ink);
  }
  .partner-mark {
    flex: none;
    width: 40px;
    height: 40px;
    border-radius: 50%;
    background: var(--ink);
  }
  .partner-festival {
    left: 80px;
    top: 1050px;
    width: 370px;
    font-size: 26px;
    line-height: 1.15;
  }
  .partner-academy {
    left: 600px;
    top: 1040px;
    width: 300px;
    font-size: 26px;
    line-height: 1.15;
  }
</style>
</head>
<body>
<main class="poster">
  <svg class="swords" width="44" height="40" viewBox="0 0 44 40" aria-hidden="true">
    <g stroke="var(--ink)" stroke-width="4" stroke-linecap="round">
      <line x1="6" y1="4" x2="38" y2="36"/>
      <line x1="38" y1="4" x2="6" y2="36"/>
      <line x1="26" y1="32" x2="34" y2="24"/>
      <line x1="18" y1="32" x2="10" y2="24"/>
    </g>
  </svg>

  <h1 class="centered title-main">SIEGE</h1>
  <p class="centered title-of"><span class="dot"></span>of<span class="dot"></span></p>
  <div class="title-rule"></div>
  <h2 class="centered title-sub"><span class="cap">M</span>ARROWFIELD <span class="cap">B</span>ALL</h2>
  <p class="centered event-date"><span class="cap">S</span>ATURDAY 11 <span class="cap">A</span>PRIL 2015</p>

  <svg class="dancers" viewBox="0 0 310 575" role="img" aria-label="Sepia photograph of a couple in Regency costume dancing, the woman in a white gown and the man in a waistcoat and breeches">
    <defs>
      <radialGradient id="dancers-tone" cx="50%" cy="48%" r="55%">
        <stop offset="0%" stop-color="var(--sepia-mid)"/>
        <stop offset="45%" stop-color="var(--sepia-light)"/>
        <stop offset="100%" stop-color="var(--paper)" stop-opacity="0"/>
      </radialGradient>
      <linearGradient id="dancers-figure" x1="0" y1="0" x2="1" y2="0">
        <stop offset="0%" stop-color="var(--sepia-light)"/>
        <stop offset="55%" stop-color="var(--sepia-mid)"/>
        <stop offset="100%" stop-color="var(--sepia-dark)" stop-opacity="0.7"/>
      </linearGradient>
    </defs>
    <ellipse cx="155" cy="295" rx="155" ry="280" fill="url(#dancers-tone)"/>
    <rect x="60" y="100" width="210" height="440" rx="90" fill="url(#dancers-figure)" opacity="0.55"/>
  </svg>

  <section class="info venue">
    <p class="info-label">VENUE</p>
    <p class="info-value">Pellham Hall,<br>Canberra</p>
  </section>

  <section class="info time">
    <p class="info-label">TIME</p>
    <p class="info-value">7.30pm-11.30pm</p>
  </section>

  <section class="info cost">
    <p class="info-label">COST</p>
    <p class="info-value">to be announce</p>
  </section>

  <section class="info tickets">
    <p class="info-label">TICKETS</p>
    <p class="info-label small">ON SALE AT</p>
    <p class="info-value url">www.clarawhitbyfestival.example.au</p>
  </section>

  <p class="centered festival-line"><span class="cap">C</span>LARA <span class="cap">W</span>HITBY <span class="cap">F</span>ESTIVAL <span class="cap">A</span>USTRALIA<br>2015</p>

  <div class="partner partner-festival">
    <span class="partner-mark"></span>
    <span>Clara Whitby Festival Australia</span>
  </div>

  <div class="partner partner-academy">
    <span class="partner-mark"></span>
    <span>Velvet Lantern Historic Dance Academy</span>
  </div>
</main>
</body>
</html>
```